Holiday Club Flyer for the Autumn half term school holidays for children aged 4 - 11 years old

Hi Please can someone adapt the attached flyer to reflect the new theme which is Deep Sea Divers. The dates need to be changed to 30th, 31st October and 1st November. Instead of saying mission can it say dive dates, dive location and dive times. Can you remove picnic lunch and just say lunch provided. Under the Dive times box instead of saying picnic lunch 12-12:30 can it just say collection @ 12:30.

Target Market(s)

Children aged between 4 - 11 years old

Requirements
Must have
• Eye catching and interesting for children, easy to read information and be bold.

```html
<!DOCTYPE html>
<html lang="en">
<head>
<meta charset="utf-8">
<title>Deep Sea Divers Holiday Club Flyer</title>
<link rel="stylesheet" href="https://fonts.googleapis.com/css2?family=Fredoka:wght@500;600;700&family=Lilita+One&family=Baloo+2:wght@500;600;700&display=swap">
<style>
  :root {
    --teal: #2bb2bd;
    --navy: #1d2b47;
    --purple: #55298c;
    --orange: #e0542a;
    --orange-soft: #ec7c3c;
    --peach: #f2b197;
    --peach-shade: #c9775a;
    --green: #7cb83b;
    --green-dark: #1f9a45;
    --yellow: #f3e44b;
    --white: #ffffff;
  }
  * { box-sizing: border-box; margin: 0; padding: 0; }
  html, body { width: 1200px; height: 800px; overflow: hidden; background: var(--white); }
  body { position: relative; font-family: "Baloo 2", sans-serif; }

  .page { position: absolute; top: 57px; width: 532px; height: 688px; overflow: hidden; }
  .page--cover { left: 56px; }
  .page--info { left: 616px; }

  /* Cover */
  .cover-photo {
    position: absolute; inset: 0;
    background:
      radial-gradient(ellipse 30% 22% at 12% 8%, rgba(238,130,70,.55), transparent 70%),
      radial-gradient(ellipse 22% 18% at 92% 8%, rgba(238,130,70,.6), transparent 70%),
      radial-gradient(ellipse 40% 38% at 80% 82%, rgba(70,50,45,.75), transparent 70%),
      radial-gradient(ellipse 32% 30% at 82% 70%, rgba(232,200,170,.5), transparent 70%),
      radial-gradient(ellipse 45% 30% at 22% 92%, rgba(240,140,80,.7), transparent 70%),
      radial-gradient(ellipse 40% 25% at 10% 70%, rgba(230,110,80,.45), transparent 70%),
      linear-gradient(180deg, #8ad8da 0%, #3bb8c2 22%, #1f9aa8 48%, #157a86 72%, #11606c 100%);
  }
  .brand { position: absolute; left: 0; width: 100%; text-align: center; }
  .brand__mark { display: block; margin: 0 auto; width: 41px; height: 41px; border-radius: 50%; background: var(--white); }
  .brand__name { font-family: "Fredoka", sans-serif; font-weight: 600; color: var(--white); font-size: 19px; margin-top: 8px; display: block; }
  .cover .brand { top: 73px; }

  .title { position: absolute; font-family: "Fredoka", sans-serif; font-weight: 700; color: var(--peach); line-height: 1; white-space: nowrap;
    -webkit-text-stroke: 6px var(--white); paint-order: stroke fill;
    text-shadow: 0 5px 0 var(--peach-shade); letter-spacing: -1px; }
  .title--top { left: 68px; top: 190px; font-size: 96px; transform: rotate(-10deg); transform-origin: left center; }
  .title--bottom { left: 84px; top: 318px; font-size: 132px; transform: rotate(-11deg); transform-origin: left center; }

  /* Info page */
  .info-scene {
    position: absolute; inset: 0;
    background: linear-gradient(180deg, #6cc9cf 0%, #3cb6c0 40%, #2894a6 62%, #1b5d7a 80%, #1f3350 100%);
  }
  .reef { position: absolute; right: 0; bottom: 50px; width: 240px; height: 320px;
    background: radial-gradient(ellipse at 60% 55%, rgba(240,150,80,.75) 0 25%, rgba(60,150,170,.6) 48%, transparent 72%); }
  .footer-band { position: absolute; left: 0; right: 0; bottom: 0; height: 44px; background: var(--navy); }

  .club-head { position: absolute; left: 33px; top: 30px; display: flex; align-items: center; gap: 10px; }
  .club-head__mark { width: 40px; height: 40px; border-radius: 50%; background: var(--green-dark); }
  .club-head__kids { font-family: "Lilita One", sans-serif; font-size: 17px; color: var(--green-dark); margin-right: 6px; }
  .club-head__title { font-family: "Lilita One", sans-serif; color: var(--purple); font-size: 25px; line-height: .85; }
  .free-tag { position: absolute; left: 247px; top: 36px; width: 40px; height: 28px; border-radius: 14px; background: var(--green);
    color: var(--yellow); font-family: "Fredoka", sans-serif; font-weight: 700; font-size: 12px; display: flex; align-items: center; justify-content: center; }

  .dive-row { position: absolute; left: 33px; border: 3px solid var(--white); border-radius: 42px; display: flex; align-items: center; }
  .dive-row--dates { top: 105px; width: 403px; height: 82px; }
  .dive-row--location { top: 201px; width: 390px; height: 82px; }
  .dive-row--times { top: 297px; width: 409px; height: 83px; }
  .dive-row__label { width: 112px; text-align: right; font-family: "Fredoka", sans-serif; font-weight: 600; color: var(--white); line-height: .95; padding-right: 2px; }
  .dive-row__label small { display: block; font-size: 21px; }
  .dive-row__label strong { display: block; font-size: 26px; font-weight: 600; }
  .dive-row__rule { width: 3px; height: 46px; background: var(--white); margin: 0 14px; }
  .dive-row__text { color: var(--white); font-weight: 700; font-size: 16.5px; line-height: 1.15; }
  .time-line { display: flex; align-items: center; gap: 14px; margin: 2px 0; }
  .time-chip { background: var(--orange); border-radius: 6px; padding: 0 5px; font-size: 16px; line-height: 20px; min-width: 50px; text-align: center; }

  .age-badge { position: absolute; left: 350px; top: 80px; width: 200px; height: 220px; border-radius: 48% 40% 44% 52%;
    background: radial-gradient(circle at 55% 50%, var(--orange-soft), var(--orange) 70%); transform: rotate(-10deg); }
  .age-text { position: absolute; left: 400px; top: 150px; width: 124px; text-align: center; color: var(--white); font-weight: 700; line-height: 1; }
  .age-text__for { font-size: 17px; }
  .age-text__range { font-family: "Lilita One", sans-serif; font-size: 38px; margin: 3px 0 2px; }
  .age-text__who { font-size: 15px; }

  .features { position: absolute; left: 34px; top: 396px; width: 340px; font-family: "Fredoka", sans-serif; font-weight: 600; color: var(--purple); font-size: 23px; line-height: 1.15; }

  .note-box { position: absolute; left: 33px; width: 257px; background: var(--orange); border-radius: 4px; color: var(--white); }
  .note-box--drop { top: 466px; height: 67px; padding: 9px 17px; font-size: 13px; line-height: 1.25; font-weight: 500; }
  .note-box--drop b { font-weight: 700; }
  .note-box--drop small { font-size: 11px; display: block; }
  .note-box--register { top: 597px; height: 67px; padding: 9px 24px; font-size: 13px; line-height: 1.3; font-weight: 500; }
  .note-box--register .label { font-size: 10.5px; color: #ffd9c8; }

  .find-us { position: absolute; left: 38px; top: 546px; display: flex; gap: 8px; color: var(--white); font-size: 11.5px; line-height: 1.2; font-weight: 600; }
  .find-us .label { font-weight: 500; font-size: 10.5px; }

  .info-brand { position: absolute; left: 345px; top: 571px; width: 170px; text-align: center; }
  .info-brand .brand__mark { width: 38px; height: 38px; }
  .info-brand .brand__name { font-size: 16px; margin-top: 4px; }
  .site-url { position: absolute; left: 345px; width: 170px; top: 652px; text-align: center; color: var(--yellow); font-size: 13px; font-weight: 600; }
</style>
</head>
<body>

<section class="page page--cover cover">
  <div class="cover-photo" role="img" aria-label="Underwater coral reef photograph with bubbles, starfish and a child in a diving helmet"></div>
  <div class="brand">
    <span class="brand__mark"></span>
    <span class="brand__name">Harbour Lane Church</span>
  </div>
  <h1>
    <span class="title title--top">Deep Sea</span>
    <span class="title title--bottom">Divers</span>
  </h1>
</section>

<section class="page page--info">
  <div class="info-scene" role="img" aria-label="Illustrated underwater scene with light rays and rocks"></div>
  <div class="reef" role="img" aria-label="Illustrated coral reef and seaweed"></div>
  <div class="footer-band"></div>

  <header class="club-head">
    <span class="club-head__mark"></span>
    <span class="club-head__kids">SeaKids</span>
    <span class="club-head__title">holiday<br>club</span>
  </header>
  <div class="free-tag">FREE!</div>

  <div class="dive-row dive-row--dates">
    <div class="dive-row__label"><small>DIVE</small><strong>Dates</strong></div>
    <div class="dive-row__rule"></div>
    <div class="dive-row__text">30th, 31st October<br>&amp; 1st November</div>
  </div>
  <div class="dive-row dive-row--location">
    <div class="dive-row__label"><small>DIVE</small><strong>Location</strong></div>
    <div class="dive-row__rule"></div>
    <div class="dive-row__text">Harbour Lane Church<br>Lantern Row</div>
  </div>
  <div class="dive-row dive-row--times">
    <div class="dive-row__label"><small>DIVE</small><strong>Times</strong></div>
    <div class="dive-row__rule"></div>
    <div class="dive-row__text">
      <div class="time-line"><span class="time-chip">8:45</span>Drop-off &amp; Registration</div>
      <div class="time-line"><span class="time-chip">12:30</span>Collection</div>
    </div>
  </div>

  <div class="age-badge" role="img" aria-label="Illustrated orange starfish"></div>
  <div class="age-text">
    <div class="age-text__for">FOR</div>
    <div class="age-text__range">4-11</div>
    <div class="age-text__who">YEAR OLDS!</div>
  </div>

  <p class="features">Featuring Games, Bible Stories, Quizzes, Craft &amp; more!</p>

  <div class="note-box note-box--drop">
    <b>Drop off from 8:45</b><br>
    Collect your children @ 12:30pm
    <small>(with a lunch provided for children)</small>
  </div>

  <div class="find-us">
    <svg width="12" height="16" viewBox="0 0 12 16" aria-hidden="true"><path d="M6 0a6 6 0 0 0-6 6c0 4.5 6 10 6 10s6-5.5 6-10a6 6 0 0 0-6-6zm0 8.5A2.5 2.5 0 1 1 6 3.5a2.5 2.5 0 0 1 0 5z" fill="#e0542a"/></svg>
    <div><span class="label">FIND US:</span><br>Harbour Lane Church, Lantern Row,<br>Marlow, ML4 2QT</div>
  </div>

  <div class="note-box note-box--register">
    <span class="label">REGISTER AT</span><br>
    https://holidayclub.harbourlane.org<br>
    holidayclub@harbourlane.org
  </div>

  <div class="info-brand brand">
    <span class="brand__mark"></span>
    <span class="brand__name">Harbour Lane Church</span>
  </div>
  <div class="site-url">www.harbourlane.org</div>
</section>

</body>
</html>
```